Technology Enablement - One Pager

I need (2) one pager piece of marketing collateral to use as outreach for a service offering. The one pager must have a strong call to action, highlight the pain points the service solves.

```html
<!DOCTYPE html>
<html lang="en">
<head>
<meta charset="utf-8">
<title>Norventa – Technology Enablement One Pagers</title>
<link rel="stylesheet" href="https://fonts.googleapis.com/css2?family=Noto+Sans:ital,wght@0,400;0,500;0,600;0,700;1,400&display=swap">
<style>
  :root {
    --stage: #1b3447;
    --ink: #1d3246;
    --body: #2c3a46;
    --accent: #1a8ec8;
    --paper: #ffffff;
    --paper-soft: #f7f8f9;
    --paper-grey: #ecf0f3;
    --pointer: #f2a51f;
  }
  * { box-sizing: border-box; margin: 0; padding: 0; }
  html, body { width: 953px; height: 1200px; overflow: hidden; background: var(--stage); }
  body { font-family: "Noto Sans", sans-serif; color: var(--body); }

  .board {
    position: absolute; left: 0; top: 0;
    width: 1712px; height: 2156px;
    transform: scale(0.5567); transform-origin: 0 0;
  }
  .page { position: absolute; width: 651px; height: 918px; background: var(--paper); overflow: hidden; }
  .page--smb { left: 185px; top: 143px; }
  .page--trades { left: 876px; top: 143px; }
  .page--smb-offer { left: 185px; top: 1095px; background: linear-gradient(160deg, #f1f4f6 0%, #e9eef1 60%, #eef2f5 100%); }
  .page--trades-offer { left: 876px; top: 1095px; background: linear-gradient(160deg, #f1f4f6 0%, #e9eef1 60%, #eef2f5 100%); border-top: 13px solid var(--paper); }

  .block { position: absolute; left: 60px; z-index: 2; white-space: nowrap; }
  .body-text { font-size: 11.5px; line-height: 18.5px; color: var(--body); }
  .list { list-style: none; font-size: 11.5px; line-height: 18.5px; color: var(--body); }
  .list li::before { content: "•"; margin-right: 6px; font-size: 9px; vertical-align: 1px; }
  .lead { font-size: 14px; line-height: 23px; color: var(--ink); }
  .title { font-size: 25px; font-weight: 600; color: var(--ink); line-height: 1.2; }
  .heading { font-size: 17px; font-weight: 600; color: var(--ink); line-height: 1.2; }
  .section-title { font-size: 25px; font-weight: 600; color: var(--accent); line-height: 1.2; }
  .product-title { font-size: 18px; font-weight: 600; color: var(--ink); line-height: 1.2; }
  .label { font-size: 11.5px; font-weight: 700; color: var(--ink); line-height: 18.5px; }
  .label--accent { color: var(--accent); }
  .strong { font-weight: 700; color: var(--ink); }
  .cta-link { font-size: 11.5px; font-weight: 700; color: var(--accent); line-height: 18.5px; }
  .cta-link .pointer { color: var(--pointer); margin-right: 4px; }

  .brand { position: absolute; left: 60px; top: 62px; display: flex; align-items: center; gap: 9px; z-index: 2; }
  .brand-mark { width: 40px; height: 40px; border-radius: 50%; background: var(--accent); }
  .brand-name { font-size: 31px; font-weight: 500; color: var(--accent); letter-spacing: 2px; }

  .soft-panel { position: absolute; left: 0; top: 322px; width: 651px; height: 596px; background: var(--paper-soft); z-index: 0; }
  .photo { position: absolute; z-index: 1; }
  .photo--smb { left: 375px; top: 330px; width: 276px; height: 588px;
    background:
      linear-gradient(90deg, rgba(247,248,249,1) 0%, rgba(247,248,249,0.85) 25%, rgba(247,248,249,0) 60%),
      linear-gradient(180deg, rgba(160,170,190,0.15) 0%, #9aa3bf 35%, #5a6899 70%, #2c3a70 100%); }
  .photo--trades { left: 344px; top: 617px; width: 307px; height: 301px;
    background: radial-gradient(ellipse at 72% 55%, #b9c0c8 0%, #d8dde2 45%, rgba(255,255,255,0) 72%); }
  .network { position: absolute; left: 324px; top: 0; width: 327px; height: 257px; z-index: 1;
    background: radial-gradient(ellipse at 80% 20%, rgba(150,200,215,0.28) 0%, rgba(255,255,255,0) 70%); }
</style>
</head>
<body>
<main class="board">

  <section class="page page--smb">
    <div class="soft-panel"></div>
    <div class="photo photo--smb" role="img" aria-label="Photo of a businessman in glasses holding a phone, blended with a city skyline"></div>

    <div class="brand"><span class="brand-mark"></span><span class="brand-name">NORVENTA</span></div>

    <h1 class="block title" style="top:140px">Technology Enablement – SMB</h1>
    <p class="block lead" style="top:189px">Your technology shouldn’t slow your business down.<br>We help SMBs turn disconnected tools into systems that actually work.</p>

    <h2 class="block heading" style="top:252px">The Problem</h2>
    <p class="block body-text" style="top:283px">Most growing businesses have plenty of software — but no real system.<br>You’ve invested in cloud tools, CRMs, accounting platforms, HR apps, and automation.<br>Yet day-to-day work still feels harder than it should.</p>

    <h2 class="block heading" style="top:347px">Common pain points</h2>
    <ul class="block list" style="top:378px">
      <li>Software doesn’t talk to each other</li>
      <li>Key processes live in people’s heads</li>
      <li>Manual work fills the gaps between systems</li>
      <li>Decisions are made without clear data</li>
      <li>Tech choices are made reactively, not strategically</li>
    </ul>
    <p class="block body-text" style="top:481px">The result?<br>More effort, more admin, and less return on your software spend.</p>

    <h2 class="block section-title" style="top:530px">What We Do</h2>
    <p class="block body-text" style="top:571px">Technology Enablement is about improving how work actually flows through your business.<br>Norventa helps you:</p>
    <ul class="block list" style="top:614px">
      <li>Identify workflow and process gaps</li>
      <li>Find where technology is creating friction (not value)</li>
      <li>Improve adoption of the tools you already pay for</li>
      <li>Clarify where automation and integration will actually help</li>
      <li>Build a practical roadmap tied to real business outcomes</li>
    </ul>
    <p class="block body-text" style="top:718px">This is not IT support.<br>It’s operational improvement, using technology as the lever.</p>

    <h2 class="block section-title" style="top:776px">Our Approach Is Different</h2>
    <ul class="block list" style="top:816px">
      <li>You do not need to switch IT providers</li>
      <li>You do not need to rip and replace systems</li>
      <li>You do not need a long-term contract</li>
    </ul>
  </section>

  <section class="page page--trades">
    <div class="network" role="img" aria-label="Faint connected-dots network decoration"></div>
    <div class="photo photo--trades" role="img" aria-label="Illustration of a man in a VR headset reaching out, surrounded by wireframe network lines"></div>

    <h1 class="block title" style="top:62px">Technology Enablement for Trades</h1>
    <p class="block" style="top:99px;font-size:13px;font-style:italic;color:var(--ink)">(Electrical, Plumbing, HVAC, Mechanical, Construction)</p>
    <h2 class="block" style="top:138px;font-size:21px;font-weight:600;color:var(--accent)">Your jobs are physical. Your problems aren’t.</h2>
    <p class="block" style="top:176px;font-size:13px;color:var(--ink)">We help trade businesses fix the tech and workflows behind the work.</p>

    <h2 class="block heading" style="top:217px;font-size:16px">The Reality in the Trades</h2>
    <p class="block body-text" style="top:246px">Trade companies rely on technology more than ever — even if they don’t call it “IT.”<br>Scheduling. Estimating. Job tracking. Invoicing. Payroll. Field apps.<br>Most of it works… kind of.</p>

    <h2 class="block heading" style="top:320px;font-size:16px">Common frustrations:</h2>
    <ul class="block list" style="top:352px">
      <li>Office and field systems don’t line up</li>
      <li>Dispatch process is manual or inefficient.</li>
      <li>Jobs get quoted one way and invoiced another</li>
      <li>Information is stuck in texts, notebooks, or someone’s phone</li>
      <li>Admin work grows faster than revenue</li>
      <li>Technology decisions fall to “whoever knows computers”</li>
    </ul>
    <p class="block body-text" style="top:473px;color:var(--ink)">The work gets done — but it takes more effort than it should.</p>

    <h2 class="block section-title" style="top:506px">What We Do</h2>
    <p class="block body-text" style="top:546px">We help trade companies simplify operations using technology they already depend on.<br>Norventa focuses on:</p>
    <ul class="block list" style="top:589px">
      <li>How work flows from quote → job → invoice → reporting</li>
      <li>How office and field tools connect (or don’t)</li>
      <li>Where manual steps create delays, rework, or missed revenue</li>
      <li>Why tools aren’t being fully used by crews or admin staff</li>
    </ul>
    <p class="block body-text" style="top:668px">This is about making the business easier to run — not selling IT jargon.</p>

    <h2 class="block section-title" style="top:707px">Our Approach Is Different</h2>
    <ul class="block list" style="top:753px">
      <li>Low-risk, practical, and clear</li>
      <li>No pressure to replace systems</li>
      <li>No requirement to change IT providers</li>
      <li>Focused on productivity, not tech for tech’s sake</li>
    </ul>
    <p class="block body-text" style="top:837px">We earn trust by fixing real problems first.</p>
  </section>

  <section class="page page--smb-offer">
    <p class="block body-text" style="top:51px">We start with clarity first.<br>Execution comes later — only where it makes sense.</p>

    <h2 class="block product-title" style="top:108px">Product 1: Technology Enablement Assessment</h2>
    <p class="block label" style="top:135px">A 2–4 week, stand-alone engagement</p>
    <p class="block body-text" style="top:163px">We assess your:</p>
    <ul class="block list" style="top:187px">
      <li>Technology &amp; digital maturity</li>
      <li>Core workflows and handoffs</li>
      <li>Integration and automation opportunities</li>
      <li>Adoption gaps and training needs</li>
      <li>Data, reporting, and KPI visibility</li>
      <li>IT and security posture (at a business level)</li>
    </ul>

    <p class="block label" style="top:312px">You receive:</p>
    <p class="block body-text" style="top:331px">A prioritized <span class="strong">5–10 item Improvement Roadmap,</span> each with:</p>
    <ul class="block list" style="top:358px">
      <li>Business impact</li>
      <li>Relative effort</li>
      <li>ROI potential</li>
    </ul>
    <p class="block body-text" style="top:423px"><span class="strong">Price:</span> $2,500<br>No upsell required. No obligation beyond the assessment.</p>

    <h3 class="block label label--accent" style="top:474px">Who This Is For</h3>
    <ul class="block list" style="top:501px">
      <li>Small and mid-sized businesses</li>
      <li>Leadership teams feeling “tech pressure” but lacking a plan</li>
      <li>Companies scaling headcount faster than systems</li>
      <li>Owners tired of guessing which tools to buy next</li>
    </ul>

    <h3 class="block label label--accent" style="top:590px">Why Start Here</h3>
    <p class="block body-text" style="top:614px">Because buying more software without fixing workflows just adds complexity.<br>This assessment gives you:</p>
    <ul class="block list" style="top:658px">
      <li>Clarity instead of opinions</li>
      <li>A roadmap instead of random fixes</li>
      <li>Confidence before spending more money</li>
    </ul>

    <h3 class="block label label--accent" style="top:729px">Call to Action</h3>
    <p class="block body-text" style="top:753px"><span class="strong">Start with insight. Move forward with confidence.</span><br>Let’s identify what’s actually holding your business back — and how to fix it.</p>
    <p class="block cta-link" style="top:799px"><span class="pointer">➜</span>Book a Technology Enablement Assessment</p>
  </section>

  <section class="page page--trades-offer">
    <h2 class="block product-title" style="top:39px">Product 1: Trades Technology Enablement Assessment</h2>
    <p class="block label" style="top:64px">A 2–4 week, stand-alone assessment built specifically for trades</p>
    <p class="block body-text" style="top:97px">We review:</p>
    <ul class="block list" style="top:121px">
      <li>Job management workflows</li>
      <li>Quoting → scheduling → invoicing flow</li>
      <li>Field tools and adoption gaps</li>
      <li>Office vs field handoffs</li>
      <li>Reporting visibility (jobs, labour, margins)</li>
      <li>Security and data risks (without fear tactics)</li>
    </ul>

    <p class="block label" style="top:243px">You receive:<br>A Trades-Specific Improvement Roadmap showing:</p>
    <ul class="block list" style="top:292px">
      <li>Where time and money are being lost</li>
      <li>What to fix first</li>
      <li>What can wait</li>
      <li>Where automation or integration actually pays off</li>
    </ul>
    <p class="block body-text" style="top:373px;left:63px">Price:$2,500<br>Straightforward. No obligation beyond the assessment.</p>

    <h3 class="block label" style="top:426px">Who This Is For</h3>
    <ul class="block list" style="top:454px">
      <li>Electrical, plumbing, HVAC, mechanical, GC, and construction firms</li>
      <li>Owners feeling buried in admin</li>
      <li>Companies growing past “winging it”</li>
      <li>Trades relying on multiple apps that don’t work well together</li>
    </ul>

    <h3 class="block label" style="top:545px">Why Start With an Assessment</h3>
    <p class="block body-text" style="top:574px">Because buying more software without fixing workflows just adds complexity.<br>This assessment gives you:</p>
    <p class="block body-text" style="top:617px">Because guessing costs more than clarity.<br>This gives you:</p>

    <h3 class="block label" style="top:672px">Call to Action</h3>
    <p class="block label" style="top:694px">Fix the systems behind the scenes — so the work runs smoother on site.</p>
    <p class="block cta-link" style="top:723px"><span class="pointer">➜</span>Book a Trades Technology Enablement Assessment</p>
  </section>

</main>
</body>
</html>
```